Birch Hollow Lodge & Harbour. A site that will sell our lifestyle and embody our vision.

We are after a fun interactive website for our property development.
Check out our ideas for layout and content.
Use stock videos and phots if we havent provide enough.
Ive attached our Logo.
We are easy to reach and work with. Love the crative process.1.Our Vision.. (This clicks through to vision page)
Nestled in the North East corner of Tesko Lake , Sk amidst thousands of acres of natural beauty, a unique community is taking shape. A community that connectS people, nature and play. A place to find those simpler times.

2.Explore..(This clicks through to explore page)
Discover a new life of adventure, on the lake fishing, in the bush on our trail system or maybe the local golf course.

3. Live Here..(This through to Live page)
Birch Hollow has everything you need to start living a full life based in a thriving community.
Slow down and get to know nature and your neighbors

Target Market(s)

35-65 Lake Life

Coding

Coded - Design and coding required

Number of Pages Required

5+ page

Font styles to use
Other font styles liked:
• Anntonio

Colors
00AB8E
00BBA5
67D7C9
C6EFE9
E9F9F6
F0912C
F2A743
F7CA91
FBE8D2
FDF5EE

Requirements
Nice to have
• Interactive

```html
<!DOCTYPE html>
<html lang="en">
<head>
<meta charset="utf-8">
<title>Birch Hollow Lodge &amp; Harbour</title>
<link href="https://fonts.googleapis.com/css2?family=Antonio:wght@600;700&family=Rubik:wght@400;500&family=Ubuntu:wght@400;500&display=swap" rel="stylesheet">
<style>
  :root{
    --teal:#1b6e6e;
    --teal-light:#4f9a8b;
    --deep:#003a3c;
    --bar:#3f877a;
    --orange:#f96a25;
    --paper:#f0f0f0;
    --ink:#3d4a52;
    --text:#4a4f53;
    --people:#aebfcc;
    --nature:#5fb8a8;
    --play:#1f8cc6;
    --hex-line:#c5d2d3;
  }
  *{margin:0;padding:0;box-sizing:border-box}
  html,body{width:1012px;height:1200px;overflow:hidden}
  body{position:relative;background:var(--paper);font-family:"Rubik",sans-serif;color:var(--text)}
  .abs{position:absolute}

  .hero{left:0;top:0;width:1012px;height:492px;
    background:linear-gradient(180deg,#5f676b 0%,#55605a 22%,#4a5535 45%,#3d4a34 62%,#3a4445 78%,#2e3a36 100%)}
  .hero-peak{left:0;top:455px;width:1012px;height:38px}
  .menu-btn{left:127px;top:21px;width:29px;height:26px;background:var(--teal);border-radius:2px}
  .menu-btn span{position:absolute;right:7px;height:1.6px;background:#fff;border-radius:1px}
  .contact-btn{left:800px;top:21px;width:86px;height:26px;background:var(--teal);color:#fff;
    font:500 8.6px/26px "Rubik",sans-serif;letter-spacing:.6px;text-align:center;border-radius:2px}
  .brand{left:406px;top:48px;width:200px;text-align:center;color:#fff;
    font:700 22px/1.1 "Antonio",sans-serif;letter-spacing:1px;text-transform:uppercase}

  .hero-copy{left:306px;top:228px;width:400px;text-align:center;color:#fff}
  .hero-kicker{font:500 12px/1 "Ubuntu",sans-serif;letter-spacing:.3px}
  .hero-title{font:700 36px/1 "Antonio",sans-serif;margin-top:5px;letter-spacing:.2px}
  .hero-title .people{color:var(--people)}
  .hero-title .nature{color:var(--nature)}
  .hero-title .play{color:var(--play)}
  .hero-sub{font:400 14px/1 "Ubuntu",sans-serif;margin-top:3px}
  .pricing-btn{left:437px;top:310px;width:139px;height:26px;background:var(--orange);color:#fff;
    font:500 8.6px/26px "Rubik",sans-serif;letter-spacing:.6px;text-align:center;border-radius:2px}
  .scroll-cue{left:499px;top:484px}

  .feature{top:571px;width:200px;text-align:center}
  .feature svg{display:block;margin:0 auto}
  .feature h2{font:700 27px/1.05 "Antonio",sans-serif;color:var(--ink);text-transform:uppercase;margin-top:16px;letter-spacing:.2px}
  .feature p{font:400 9px/12.7px "Rubik",sans-serif;color:var(--text);margin:12px auto 0}
  .vision{left:174px} .vision p{width:180px}
  .explore{left:406px} .explore p{width:190px}
  .live{left:628px;width:220px} .live p{width:212px}
  .more-btn{left:444px;top:848px;width:124px;height:26px;background:var(--teal);color:#fff;
    font:500 8.6px/26px "Rubik",sans-serif;letter-spacing:.6px;text-align:center;border-radius:2px}

  .footer{left:0;top:968px;width:1012px;height:205px;background:var(--deep)}
  .footer-peak{left:0;top:932px;width:1012px;height:37px}
  .social{top:1030px;width:27px;height:27px;border-radius:50%;background:var(--teal)}
  .social.active{background:var(--orange)}
  .footer-brand{left:436px;top:1060px;width:140px;text-align:center;color:#fff;
    font:700 19px/1.1 "Antonio",sans-serif;letter-spacing:1px;text-transform:uppercase}
  .touch-title{left:657px;top:1017px;color:#fff;font:700 18px/1 "Antonio",sans-serif;text-transform:uppercase}
  .subscribe{left:657px;top:1045px;width:213px;height:25px;border:1px solid #1c5a5a;border-radius:2px}
  .subscribe span{position:absolute;left:10px;top:0;font:400 9px/23px "Rubik",sans-serif;color:#2f7670}
  .subscribe .send{position:absolute;right:1px;top:1px;width:22px;height:21px;background:var(--teal);border-radius:2px}
  .footer-nav{top:1133px;font:400 10.5px/1 "Rubik",sans-serif;color:#fff}
  .footer-nav.current{color:var(--orange);text-decoration:underline}

  .legal{left:0;top:1173px;width:1012px;height:27px;background:var(--bar);color:#fff;
    font:400 9.6px/27px "Rubik",sans-serif;text-align:center}
  .legal .sep{color:#6fa89c;margin:0 7px}
</style>
</head>
<body>

<section class="abs hero" role="img" aria-label="Photograph of lakeside homes, a green lawn and a marina with boat lifts reflected in calm water under an autumn sky"></section>
<svg class="abs hero-peak" width="1012" height="38" viewBox="0 0 1012 38">
  <polygon points="338,37 506,3 674,37" fill="var(--teal-light)"/>
  <polygon points="0,37 338,37 506,9 674,37 1012,37 1012,38 0,38" fill="var(--paper)"/>
</svg>

<div class="abs menu-btn" aria-label="Menu">
  <span style="top:8px;width:14px"></span>
  <span style="top:12.5px;width:14px"></span>
  <span style="top:17px;width:9px"></span>
</div>
<div class="abs contact-btn">CONTACT US</div>
<div class="abs brand">Birch Hollow<br>Lodge &amp; Harbour</div>

<div class="abs hero-copy">
  <div class="hero-kicker">CONNECT TO</div>
  <div class="hero-title"><span class="people">PEOPLE,</span> <span class="nature">NATURE,</span> <span class="play">PLAY</span></div>
  <div class="hero-sub">Marina Lots with Lake access for sale</div>
</div>
<div class="abs pricing-btn">VIEW OUR PRICING MAP</div>

<svg class="abs scroll-cue" width="14" height="30" viewBox="0 0 14 30" fill="none" stroke="#3d4a52" stroke-width="1">
  <rect x="1" y="1" width="12" height="18" rx="6"/>
  <line x1="7" y1="5" x2="7" y2="8"/>
  <line x1="7" y1="22" x2="7" y2="29"/>
  <polyline points="4,26 7,29 10,26"/>
</svg>

<div class="abs feature vision">
  <svg width="64" height="82" viewBox="0 0 64 82">
    <polygon points="1,19 32,1 63,19 63,81 1,81" fill="none" stroke="var(--hex-line)" stroke-width="1.3"/>
    <g fill="var(--teal-light)" stroke="var(--teal-light)">
      <polygon points="20,39 47,29 50,37 23,47" stroke="none"/>
      <rect x="14" y="40" width="5" height="6" stroke="none"/>
      <line x1="33" y1="44" x2="25" y2="64" stroke-width="2"/>
      <line x1="33" y1="44" x2="41" y2="64" stroke-width="2"/>
      <line x1="33" y1="44" x2="33" y2="64" stroke-width="2"/>
    </g>
  </svg>
  <h2>Our Vision</h2>
  <p>Nestled in the North corner of Tesko Lake , Sk amidst thousands of acres of natural beauty, a unique community is taking shape. A community that connects people, nature and play. A place to find those simpler times.</p>
</div>

<div class="abs feature explore">
  <svg width="64" height="82" viewBox="0 0 64 82">
    <polygon points="1,19 32,1 63,19 63,81 1,81" fill="none" stroke="var(--hex-line)" stroke-width="1.3"/>
    <circle cx="32" cy="44" r="15" fill="none" stroke="var(--teal-light)" stroke-width="2"/>
    <polygon points="32,30 34.5,41.5 46,44 34.5,46.5 32,58 29.5,46.5 18,44 29.5,41.5" fill="var(--teal)"/>
    <polygon points="32,37 36,40 39,44 36,48 32,51 28,48 25,44 28,40" fill="var(--teal)" opacity=".6"/>
  </svg>
  <h2>Explore our<br>Ammenities</h2>
  <p>Discover &nbsp;a new life of adventure , on the lake fishing, in the bush on our trail system the local golf course or stay simple and enjoy our epic community amenities.</p>
</div>

<div class="abs feature live">
  <svg width="64" height="82" viewBox="0 0 64 82">
    <polygon points="1,19 32,1 63,19 63,81 1,81" fill="none" stroke="var(--hex-line)" stroke-width="1.3"/>
    <g fill="none" stroke="var(--teal-light)" stroke-width="2.8" stroke-linecap="round">
      <path d="M25,38 a9,9 0 0 0 0,12"/>
      <path d="M39,38 a9,9 0 0 1 0,12"/>
      <path d="M20,33 a16,16 0 0 0 0,22"/>
      <path d="M44,33 a16,16 0 0 1 0,22"/>
    </g>
    <circle cx="32" cy="44" r="3.5" fill="var(--teal)"/>
  </svg>
  <h2>Live Here</h2>
  <p>Birch Hollow Lodge And Harbour has everything you need to start living a full life , based in a thriving community. Birch Hollow Lodge And Harbour consist of 31 beautiful titled lots and 62 boat slips in an inland marina, absolutely perfect for your dream lake life. Topped with amazing amenities and facilities, &nbsp;lake life has never been better! Slow down and get to know nature and your neighbors.</p>
</div>

<div class="abs more-btn">WANT TO KNOW MORE</div>

<svg class="abs footer-peak" width="1012" height="37" viewBox="0 0 1012 37">
  <polygon points="338,36 506,2 674,36" fill="var(--teal-light)"/>
  <polygon points="0,36 338,36 506,8 674,36 1012,36 1012,37 0,37" fill="var(--deep)"/>
</svg>
<footer class="abs footer"></footer>

<div class="abs social" style="left:209px" aria-label="Social profile"></div>
<div class="abs social" style="left:243px" aria-label="Social profile"></div>
<div class="abs social active" style="left:278px" aria-label="Social profile"></div>
<div class="abs social" style="left:312px" aria-label="Social profile"></div>

<div class="abs footer-brand">Birch Hollow<br>Lodge &amp; Harbour</div>

<div class="abs touch-title">Stay in touch</div>
<div class="abs subscribe">
  <span>Your email address*</span>
  <div class="send">
    <svg width="22" height="21" viewBox="0 0 22 21" fill="none" stroke="#fff" stroke-width="1.1">
      <polygon points="7,6 16,10.5 7,15"/>
    </svg>
  </div>
</div>

<div class="abs footer-nav current" style="left:353px">Home</div>
<div class="abs footer-nav" style="left:405px">Our Vision</div>
<div class="abs footer-nav" style="left:478px">Explore</div>
<div class="abs footer-nav" style="left:537px">Live Here</div>
<div class="abs footer-nav" style="left:605px">Contact Us</div>

<div class="abs legal">© 2023 Birch Hollow Resort. All Right Reserved<span class="sep">|</span>Privacy Policy<span class="sep">|</span>Terms &amp; Conditions</div>

</body>
</html>
```